Brovatik Support Services Brochure and Flyer

I need a brochure and DL flyer created for a business that provides staff to people who live with disability and mental health. The wording is available, just looking for some clean designs with images that show natural people. I am also looking for something professional and catchy.

```html
<!DOCTYPE html>
<html lang="en">
<head>
<meta charset="utf-8">
<title>Brovatik Support Services – DL Brochure</title>
<link href="https://fonts.googleapis.com/css2?family=Lato:wght@300;400;700;900&display=swap" rel="stylesheet">
<style>
:root{
  --blue:#1f50a6;
  --blue-deep:#153a82;
  --blue-light:#3a6fc4;
  --orange:#f2a12c;
  --orange-deep:#e08a17;
  --ink:#3d3d3d;
  --paper:#ffffff;
  --paper-warm:#f6f3ee;
  --stage:#e3e3e1;
}
*{box-sizing:border-box;margin:0;padding:0}
html,body{width:1200px;height:2400px;overflow:hidden}
body{background:var(--stage);font-family:'Lato',sans-serif;color:var(--ink);position:relative}
.spread{position:absolute;left:15px;width:1170px;height:827px;display:flex;box-shadow:0 10px 30px rgba(0,0,0,.18)}
.spread--outside{top:313px}
.spread--inside{top:1260px}
.panel{position:relative;width:390px;height:827px;overflow:hidden;background:var(--paper)}
.photo{position:absolute;left:0;right:0}
.deco{position:absolute;left:0;width:100%}
.heading{font-weight:900;text-transform:uppercase;letter-spacing:.5px}
.copy{font-size:14px;line-height:1.55}

/* Why work with us */
.why .photo{top:0;height:330px;background:linear-gradient(135deg,#5d6670,#2f363d 55%,#8a8f94)}
.why__body{position:absolute;top:360px;left:34px;right:30px}
.why .heading{color:var(--orange-deep);font-size:19px;margin-bottom:6px}
.rule{height:2px;width:90px;background:var(--blue);margin-bottom:14px}
.why .copy{margin-bottom:12px;font-size:13.5px}
.why__note{position:absolute;left:0;right:0;bottom:0;height:150px;background:var(--orange);color:#fff;padding:28px 34px;font-size:14px;line-height:1.55}

/* About us */
.about{background:linear-gradient(180deg,var(--blue-light),var(--blue) 40%,var(--blue-deep))}
.about__badge{position:absolute;top:48px;left:135px;width:120px;height:120px;border-radius:50%;border:7px solid var(--orange);background:linear-gradient(180deg,#f4b24a,#e58a2c 60%,#b5611d)}
.about__name{position:absolute;top:188px;left:0;right:0;text-align:center;color:#fff}
.brand{font-weight:700;font-size:34px;letter-spacing:.3px}
.brand-sub{font-size:12px;letter-spacing:3px;text-transform:uppercase;color:var(--orange);font-weight:700;margin-top:2px}
.about .heading{position:absolute;top:262px;left:0;right:0;text-align:center;color:var(--orange);font-size:20px}
.about .copy{position:absolute;top:300px;left:36px;right:36px;text-align:center;color:#fff;font-size:13.5px}
.about__cta{position:absolute;top:478px;left:36px;right:36px;height:30px;border-radius:15px;background:var(--orange);color:#fff;font-size:13px;font-weight:700;text-align:center;line-height:30px}
.contact{position:absolute;top:528px;left:60px;right:30px;list-style:none;color:#fff;font-size:15px}
.contact li{display:flex;gap:12px;margin-bottom:10px;line-height:1.35}
.contact svg{flex:none;margin-top:2px}
.social{position:absolute;top:690px;left:0;right:0;display:flex;justify-content:center;gap:14px}
.social span{width:24px;height:24px;border-radius:50%;border:2px solid #fff}
.about__web{position:absolute;bottom:0;left:0;right:0;height:56px;background:var(--orange);color:#fff;text-align:center;line-height:56px;font-size:17px;letter-spacing:.5px}

/* Cover */
.cover__logo{position:absolute;top:42px;left:40px;display:flex;align-items:center;gap:12px}
.cover__logo .dot{width:38px;height:38px;border-radius:50%;background:var(--orange)}
.cover__logo .brand{color:var(--blue);font-size:40px}
.cover__logo .brand-sub{font-size:11px}
.cover .photo{top:140px;height:380px;background:linear-gradient(160deg,#7fa34c,#a9c36b 45%,#e7d7c3)}
.cover__blue{position:absolute;top:470px;left:0;right:0;bottom:0}
.cover__title{position:absolute;top:580px;left:30px;right:20px;color:var(--orange);font-size:34px;font-weight:300;letter-spacing:1px;text-transform:uppercase}
.cover__sub{position:absolute;top:632px;left:30px;right:20px;color:#fff;font-size:15px;line-height:1.45}
.cover__web{position:absolute;top:752px;left:0;right:0;text-align:right;padding-right:34px;color:#fff;font-size:17px;letter-spacing:.5px}

/* Staff we supply */
.staff{background:linear-gradient(180deg,var(--blue-light),var(--blue) 35%,var(--blue-deep))}
.staff .heading{position:absolute;top:36px;left:0;right:0;text-align:center;color:#fff;font-size:18px}
.staff .copy{position:absolute;top:78px;left:28px;right:28px;color:#fff;font-size:13px}
.staff__list{position:absolute;top:232px;left:48px;right:26px;color:#fff;font-size:13px;line-height:1.45}
.staff__list li{margin-bottom:4px}
.staff__list ul{margin-left:18px;list-style:circle}
.staff .photo{top:640px;height:187px;background:linear-gradient(180deg,#d8c07a,#8a6a3e 60%,#4b3a28)}

/* Inside right */
.inside .photo{top:0;height:330px}
.provide .photo{background:linear-gradient(120deg,#2f4a22,#6f8e3e 50%,#c9d39a)}
.special .photo{background:linear-gradient(120deg,#c9d39a,#9fb06a 40%,#d9c9b8)}
.inside__body{position:absolute;top:370px;left:34px;right:30px}
.inside .heading{color:var(--blue);font-size:15px;margin-bottom:6px}
.arrow-list{list-style:none;margin-top:14px}
.arrow-list li{display:flex;gap:10px;font-size:13.5px;line-height:1.5;margin-bottom:20px}
.arrow-list svg{flex:none;margin-top:4px}
.spec-list{list-style:none;margin-top:14px}
.spec-list li{font-size:12.5px;line-height:1.45;margin-bottom:9px}
.spec-list b{color:var(--orange-deep);font-weight:900;text-transform:uppercase}
.special{background:var(--paper-warm)}
</style>
</head>
<body>

<section class="spread spread--outside" aria-label="Brochure outside">

  <article class="panel why">
    <div class="photo" role="img" aria-label="Photo of a support worker helping a person in a wheelchair out of a car"></div>
    <svg class="deco" style="top:300px" width="390" height="50" viewBox="0 0 390 50" preserveAspectRatio="none">
      <path d="M0 30 Q195 0 390 22 L390 50 L0 50Z" fill="#fff"/>
      <path d="M0 30 Q195 0 390 22" fill="none" stroke="var(--orange)" stroke-width="5"/>
    </svg>
    <div class="why__body">
      <h2 class="heading">Why work with us</h2>
      <div class="rule"></div>
      <p class="copy">Our team brings together experienced disability professionals who understand each participant's goals and work closely with families and carers.</p>
      <p class="copy">With years of experience in health and community care, our staff are trained, screened and supported to deliver safe, respectful and reliable services every day.</p>
      <p class="copy">Our service is flexible, and we tailor each plan to suit your routine, your home and the people who matter most to you.</p>
    </div>
    <p class="why__note">We are registered with the NDIS and committed to quality care, clear communication and lasting relationships with the people we support.</p>
  </article>

  <article class="panel about">
    <div class="about__badge" role="img" aria-label="Photo of a person raising their arms on a beach at sunset"></div>
    <div class="about__name">
      <div class="brand">Brovatik</div>
      <div class="brand-sub">Support Services</div>
    </div>
    <h2 class="heading">About us</h2>
    <p class="copy">Brovatik Support Services is a Perth-based staffing agency focused on recruiting and placing qualified support workers for people living with disability and mental health needs. Our mission is to make daily life simpler and create lasting, remarkable relationships.</p>
    <p class="about__cta">For more information please contact</p>
    <ul class="contact">
      <li><svg width="18" height="18" viewBox="0 0 24 24"><path d="M6.6 10.8a15 15 0 0 0 6.6 6.6l2.2-2.2c.3-.3.7-.4 1-.2 1.1.4 2.3.6 3.6.6.6 0 1 .4 1 1V20c0 .6-.4 1-1 1C10.6 21 3 13.4 3 4c0-.6.4-1 1-1h3.5c.6 0 1 .4 1 1 0 1.3.2 2.5.6 3.6.1.3 0 .7-.2 1z" fill="var(--orange)"/></svg>(08) 5550 1427</li>
      <li><svg width="18" height="18" viewBox="0 0 24 24"><rect x="2" y="5" width="20" height="14" rx="2" fill="var(--orange)"/><path d="M3 6l9 7 9-7" fill="none" stroke="#fff" stroke-width="1.6"/></svg>bookings@brovatik.com.au</li>
      <li><svg width="18" height="18" viewBox="0 0 24 24"><path d="M12 2a7 7 0 0 0-7 7c0 5 7 13 7 13s7-8 7-13a7 7 0 0 0-7-7zm0 9.5A2.5 2.5 0 1 1 12 6.5a2.5 2.5 0 0 1 0 5z" fill="var(--orange)"/></svg><span>Brovatik Support Services<br>18 Carrow Street<br>Halden WA 6990</span></li>
    </ul>
    <div class="social" aria-hidden="true"><span></span><span></span><span></span><span></span></div>
    <p class="about__web">www.brovatik.com.au</p>
  </article>

  <article class="panel cover">
    <div class="cover__logo">
      <span class="dot"></span>
      <div>
        <div class="brand">Brovatik</div>
        <div class="brand-sub">Support Services</div>
      </div>
    </div>
    <div class="photo" role="img" aria-label="Photo of a smiling carer with an older woman holding a small dog in a garden"></div>
    <svg class="cover__blue" width="390" height="357" viewBox="0 0 390 357" preserveAspectRatio="none">
      <path d="M0 70 Q200 20 390 0 L390 357 L0 357Z" fill="var(--blue)"/>
      <path d="M0 70 Q200 20 390 0 L390 18 Q200 40 0 88Z" fill="var(--orange)"/>
      <path d="M0 270 Q200 250 390 262 L390 315 Q200 300 0 318Z" fill="var(--orange)"/>
      <path d="M0 330 Q200 316 390 326 L390 357 L0 357Z" fill="var(--blue-deep)"/>
    </svg>
    <h1 class="cover__title">Support Services</h1>
    <p class="cover__sub">for people with a physical, intellectual, psychosocial, or neurological disability</p>
    <p class="cover__web">www.brovatik.com.au</p>
  </article>
</section>

<section class="spread spread--inside" aria-label="Brochure inside">

  <article class="panel staff">
    <h2 class="heading">Staff we supply</h2>
    <p class="copy">We attract and employ disability support workers, mental health support workers, service coordinators and corporate support staff. Our minimum experience, compliance and training requirements for all support workers include:</p>
    <ul class="staff__list">
      <li>6-months experience in a similar role</li>
      <li>Current police clearance (acquired within the last 3 months)</li>
      <li>A Certificate III or IV in Community Services or Individual Support</li>
      <li>NDIS worker orientation module (Quality, Safety and You)</li>
      <li>Current manual handling</li>
      <li>Medication administration</li>
      <li>Proof of working rights</li>
      <li>2 employment references</li>
      <li>Other relevant skillsets which include PEG feeding, Dysphagia, Epilepsy management, Catheter care etc.</li>
    </ul>
    <div class="photo" role="img" aria-label="Photo of a person's hand gripping a forearm crutch outdoors"></div>
  </article>

  <article class="panel inside provide">
    <div class="photo" role="img" aria-label="Photo of trees in soft sunlight in a park"></div>
    <svg class="deco" style="top:300px" width="390" height="50" viewBox="0 0 390 50" preserveAspectRatio="none">
      <path d="M0 22 Q195 6 390 16 L390 50 L0 50Z" fill="#fff"/>
      <path d="M0 22 Q195 6 390 16" fill="none" stroke="var(--orange)" stroke-width="5"/>
    </svg>
    <div class="inside__body">
      <h2 class="heading">Our support workers provide:</h2>
      <div class="rule"></div>
      <ul class="arrow-list">
        <li><svg width="14" height="14" viewBox="0 0 14 14"><path d="M2 7h9M7 3l4 4-4 4" fill="none" stroke="var(--orange)" stroke-width="2"/></svg>Assistance with daily life such as end-to-end personal care, household cleaning and light yard maintenance</li>
        <li><svg width="14" height="14" viewBox="0 0 14 14"><path d="M2 7h9M7 3l4 4-4 4" fill="none" stroke="var(--orange)" stroke-width="2"/></svg>Assistance with social &amp; community participation such as community access, events, appointments</li>
        <li><svg width="14" height="14" viewBox="0 0 14 14"><path d="M2 7h9M7 3l4 4-4 4" fill="none" stroke="var(--orange)" stroke-width="2"/></svg>Transport linked to goals such as seeking or accessing employment and other goals related activities</li>
        <li><svg width="14" height="14" viewBox="0 0 14 14"><path d="M2 7h9M7 3l4 4-4 4" fill="none" stroke="var(--orange)" stroke-width="2"/></svg>Capacity building support which includes improved social and community participation, improved relationships, improved health and wellbeing, improved life choices, improved daily living skills etc.</li>
      </ul>
    </div>
  </article>

  <article class="panel inside special">
    <div class="photo" role="img" aria-label="Photo of a smiling older woman in a wheelchair with a carer beside her"></div>
    <svg class="deco" style="top:300px" width="390" height="50" viewBox="0 0 390 50" preserveAspectRatio="none">
      <path d="M0 16 Q195 4 390 20 L390 50 L0 50Z" fill="var(--paper-warm)"/>
      <path d="M0 16 Q195 4 390 20" fill="none" stroke="var(--orange)" stroke-width="5"/>
    </svg>
    <div class="inside__body">
      <h2 class="heading">Specialised supports we provide include:</h2>
      <div class="rule"></div>
      <ul class="spec-list">
        <li><b>Dysphagia:</b> for participants who have trouble eating, drinking or swallowing safely.</li>
        <li><b>Respiratory:</b> for participants requiring help with breathing, including care of their respiratory equipment and daily routines.</li>
        <li><b>Nutrition:</b> for participants requiring help with meal planning, preparing food and maintaining a healthy diet.</li>
        <li><b>Diabetes:</b> for participants who need daily monitoring and support with insulin and blood sugar checks.</li>
        <li><b>Continence:</b> for participants who need discreet help with daily continence care and aids.</li>
        <li><b>Wound &amp; pressure care:</b> for participants who need ongoing wound dressing and pressure area checks.</li>
        <li><b>Epilepsy:</b> for participants who require seizure monitoring and support that follows their care plan.</li>
        <li><b>Other support:</b> required from time to time.</li>
      </ul>
    </div>
  </article>
</section>

</body>
</html>
```